Bay Area Construction Company

Rebrand existing business card with company colors (Red and gold) for our 100th year.
Updates

Project Deadline Extended
Reason: Lots of good ideas! Still refining the concept, with just a little more time I think we will figure out which one is perfect, thank you.

Project Deadline Extended
Reason: Still reviewing

Project Deadline Extended
Reason: Still reviewing

Project Deadline Extended
Reason: Need business cards to feature updated logo with '100 years' banner.

Project Deadline Extended

Project Deadline Extended

Target Market(s)

Construction industry, males, ages 30-60 who work for building contractors

Industry/Entity Type

Business

Font styles to use
Serif

Colors
ec1f27
fbee3e
ffffff

Requirements
Must have
• Must have the colors red, gold, and black using our existing logo (Logo is available at www.marvenstoneworks.com )
Nice to have
• Company name, try to use something construction oriented. (Hardhat, Bulldoze, etc.)

```html
<!DOCTYPE html>
<html lang="en">
<head>
<meta charset="utf-8">
<title>Marven Stoneworks – Business Card</title>
<link rel="stylesheet" href="https://fonts.googleapis.com/css2?family=Roboto:wght@400;700;900&display=swap">
<style>
  :root {
    --stage: #eeeae4;
    --red: #ec1f27;
    --red-light: #f0626a;
    --red-deep: #d41a22;
    --gold: #fbee3e;
    --gold-deep: #f5d400;
    --white: #ffffff;
  }
  * { box-sizing: border-box; margin: 0; padding: 0; }
  html, body {
    width: 1200px; height: 913px; overflow: hidden;
    background: var(--stage);
    font-family: "Roboto", Arial, sans-serif;
  }
  .stage {
    position: relative; width: 1200px; height: 913px;
    display: flex; align-items: center; justify-content: center; gap: 40px;
  }
  .card {
    position: relative; width: 540px; height: 309px; overflow: hidden;
    border-radius: 4px;
    background: linear-gradient(160deg, var(--red-light) 0%, var(--red) 45%, var(--red-deep) 100%);
    box-shadow: 0 10px 24px rgba(0,0,0,.18);
  }
  /* Front */
  .card--front { display: flex; align-items: center; justify-content: center; }
  .wordmark {
    display: flex; align-items: center; gap: 12px;
    color: var(--white); font-weight: 900; font-size: 36px; letter-spacing: .5px;
    text-transform: uppercase;
  }
  .wordmark__mark { width: 30px; height: 30px; background: var(--gold); }
  /* Back */
  .card__swoosh { position: absolute; inset: 0; width: 100%; height: 100%; }
  .wordmark--small {
    position: absolute; top: 34px; right: 40px;
    font-size: 17px; gap: 8px;
  }
  .wordmark--small .wordmark__mark { width: 14px; height: 14px; }
  .holder { position: absolute; top: 146px; right: 40px; text-align: right; }
  .holder__name { color: var(--gold); font-weight: 700; font-size: 18px; }
  .holder__title { color: var(--white); font-size: 11px; margin-top: 3px; }
  .contact { position: absolute; left: 38px; top: 110px; color: var(--white); }
  .contact__company { color: var(--gold); font-weight: 700; font-size: 17px; margin-bottom: 10px; }
  .contact__list { list-style: none; font-size: 12px; line-height: 1.55; }
  .contact__row { display: flex; gap: 10px; }
  .contact__icon { width: 14px; height: 14px; flex: none; margin-top: 2px; fill: var(--gold); }
  .contact__row--plain { padding-left: 24px; }
</style>
</head>
<body>
<main class="stage">
  <section class="card card--front" aria-label="Card front">
    <div class="wordmark"><span class="wordmark__mark"></span>Marven Stoneworks</div>
  </section>

  <section class="card card--back" aria-label="Card back">
    <svg class="card__swoosh" viewBox="0 0 540 309" aria-hidden="true">
      <path d="M0 272 C170 268 280 255 345 195 C400 140 430 70 520 22 C450 70 425 140 370 205 C300 275 160 286 0 288 Z" fill="var(--gold)"/>
      <path d="M0 298 C160 288 270 264 340 224 C270 274 150 298 0 306 Z" fill="var(--gold-deep)"/>
    </svg>

    <div class="wordmark wordmark--small"><span class="wordmark__mark"></span>Marven Stoneworks</div>

    <div class="holder">
      <p class="holder__name">Your Name</p>
      <p class="holder__title">Title</p>
    </div>

    <div class="contact">
      <p class="contact__company">Bay Area Construction</p>
      <ul class="contact__list">
        <li class="contact__row"><svg class="contact__icon" viewBox="0 0 14 14"><path d="M7 0a5 5 0 0 1 5 5c0 4-5 9-5 9S2 9 2 5a5 5 0 0 1 5-5zm0 3a2 2 0 1 0 0 4 2 2 0 0 0 0-4z"/></svg>418 Harbor Lane</li>
        <li class="contact__row contact__row--plain">Novato, CA 94945</li>
        <li class="contact__row"><svg class="contact__icon" viewBox="0 0 14 14"><path d="M1 4c0-2 2-3 6-3s6 1 6 3v1h-3V4H4v1H1zm2 2h8l2 7H1z"/></svg>415-555-0142</li>
        <li class="contact__row"><svg class="contact__icon" viewBox="0 0 14 14"><path d="M3 1h8v4H3zM1 6h12v7H1zm3 2v3h6V8z"/></svg>415-555-0187</li>
        <li class="contact__row"><svg class="contact__icon" viewBox="0 0 14 14"><path d="M0 3h14v9H0zm1 1 6 4 6-4"/></svg>info@marvenstoneworks.com</li>
      </ul>
    </div>
  </section>
</main>
</body>
</html>
```